website homepage design sample for tallowreach.com.au

Hello, I am looking to update my website to be simpler and more modern and to include space for my upcoming online courses. Please review my website tallowreach.com.au for an idea of me as a male psychologist, as well as my services. I would like it to be NOT too feminine. Target market is Men and women interested in couselling, life coaching, and online courses about relationships. Id like to keep the beach theme if possible but I am open to better ideas. thank you!

please see tallowreach.com.au for my current wordpress website.

Target Market(s)

Men and Women

Industry/Entity Type

psychology

Number of Pages Required

1 page

Requirements
Must have
• An "Online Training" Menu that includes links to "Map your Bearings" , "Lantern and Compass Workbook," "Quiet Harbour Program" "Where Did All the Summers Go" "Tending the Willow Garden"

```html
<!DOCTYPE html>
<html lang="en">
<head>
<meta charset="UTF-8">
<title>Tallowreach – Psychology &amp; Coaching</title>
<link rel="stylesheet" href="https://fonts.googleapis.com/css2?family=Montserrat:wght@500;600;700;800&family=Outfit:wght@300;400;500&family=Allura&display=swap">
<style>
:root{
  --accent:#2a9dbd;
  --ink:#1d1d1f;
  --text:#444;
  --cream:#f9f7f2;
  --sand:#f3f0ea;
  --mist:#dde9ea;
  --pale:#eef3f1;
  --white:#fff;
  --footer:#4a4c55;
}
*{box-sizing:border-box;margin:0;padding:0}
html,body{width:1200px;height:5025px;overflow:hidden}
body{background:var(--cream);font-family:"Outfit",sans-serif;color:var(--text);position:relative}
.abs{position:absolute}
.header{left:0;top:0;width:1200px;height:94px;background:var(--white);display:flex;align-items:center;padding:0 111px;justify-content:space-between}
.brand{display:flex;align-items:center;gap:12px}
.brand-dot{width:44px;height:44px;border-radius:50%;background:var(--accent)}
.brand-name{font-family:"Outfit",sans-serif;font-size:28px;font-weight:400;color:var(--accent)}
.nav{display:flex;gap:16px;font-size:14px;color:#333;align-items:center}
.nav .active{background:var(--accent);color:#fff;padding:5px 10px;border-radius:3px}
.hero{left:0;top:94px;width:1200px;height:726px;background:linear-gradient(180deg,#e9c9a8 0%,#a9c0bf 30%,#6f9aa5 45%,#cfd7cf 70%,var(--cream) 100%)}
.hero-kicker{left:111px;top:240px;color:#fff;font-family:"Montserrat",sans-serif;font-weight:500;font-size:18px}
.hero-title{left:111px;top:290px;color:#fff;font-family:"Montserrat",sans-serif;font-weight:800;font-size:56px;line-height:68px}
.btn{display:inline-flex;align-items:center;justify-content:center;border-radius:40px;font-family:"Montserrat",sans-serif;font-weight:600;font-size:16px;color:var(--ink)}
.btn-solid{background:#fff;height:66px;width:248px}
.btn-line{border:1.5px solid #333;height:58px}
.label{width:1200px;left:0;text-align:center;color:var(--accent);font-family:"Montserrat",sans-serif;font-weight:500;font-size:19px}
.heading{width:1200px;left:0;text-align:center;color:#111;font-family:"Montserrat",sans-serif;font-weight:700;font-size:40px}
.lead{left:240px;width:720px;text-align:center;font-size:15px;line-height:29px;color:#444}
.photo{border-radius:0}
.script{left:610px;top:1115px;font-family:"Allura",cursive;font-size:50px;color:#222}
.sub{font-family:"Montserrat",sans-serif;color:var(--accent);font-size:19px;line-height:28px;font-weight:500}
.body{font-size:14.5px;line-height:26px;color:#444}
.wave{left:0;width:1200px}
.services-title{left:111px;top:1908px;font-family:"Montserrat",sans-serif;font-weight:700;font-size:40px;line-height:53px;color:#111}
.list{left:111px;top:2117px;display:grid;grid-template-columns:238px 200px;row-gap:10px;font-size:15px;color:#333}
.list span{display:flex;align-items:center;gap:8px}
.band{left:0;top:2458px;width:1200px;height:462px;background:var(--mist)}
.cards{left:111px;top:2737px;display:flex;gap:25px}
.card{width:226px;height:80px;background:#fff;border-radius:3px;display:flex;align-items:center;justify-content:center;text-align:center;font-family:"Montserrat",sans-serif;font-weight:500;font-size:19px;line-height:26px;color:#222;box-shadow:0 2px 8px rgba(0,0,0,.05)}
.courses{left:0;top:2920px;width:1200px;height:748px;background:var(--pale)}
.course{width:455px}
.course-img{height:309px}
.course h3{margin-top:36px;font-family:"Montserrat",sans-serif;font-weight:600;font-size:21px;color:#222}
.course h4{margin-top:10px;font-family:"Montserrat",sans-serif;font-style:italic;font-weight:500;font-size:19px;color:#333}
.course p{margin-top:12px;font-size:15px;color:#333}
.course a{color:var(--accent);text-decoration:none}
.field{background:#fff;font-size:15px;color:#666;padding:16px 20px}
.footer{left:0;top:4546px;width:1200px}
.badge{position:absolute;left:111px}
.fcol{position:absolute;top:4600px}
.fcol h5{font-family:"Montserrat",sans-serif;font-weight:600;font-size:18px;color:#222;margin-bottom:18px}
.fcol p{font-size:14.5px;line-height:28px;color:#444;display:flex;align-items:center;gap:10px}
.bar{left:0;top:4916px;width:1200px;height:109px;background:var(--footer);display:flex;align-items:center;justify-content:space-between;padding:0 111px;color:#fff;font-size:14.5px}
.bar .brand-name{color:var(--accent);font-size:30px}
.social{display:flex;gap:12px}
.social span{width:40px;height:40px;border:1.5px solid var(--accent);border-radius:50%}
</style>
</head>
<body>

<header class="header abs">
  <div class="brand"><span class="brand-dot"></span><span class="brand-name">Tallowreach</span></div>
  <nav class="nav">
    <span>About</span><span>Counselling &amp; Therapy</span><span>Current FREE Training Programs</span><span>Courses</span><span class="active">Blog</span><span>Contact</span><span>Bookings</span>
  </nav>
</header>

<section class="hero abs" role="img" aria-label="Beach at sunrise with waves rolling onto the sand and seagulls overhead"></section>
<div class="hero-kicker abs">NEXT AVAILABLE APPOINTMENT: WITHIN 7 DAYS</div>
<h1 class="hero-title abs">PSYCHOLOGY &amp;<br>COACHING</h1>
<a class="btn btn-solid abs" style="left:111px;top:464px">BOOK APPOINTMENT</a>

<div class="label abs" style="top:834px">ABOUT</div>
<h2 class="heading abs" style="top:882px">WELCOME TO TALLOWREACH</h2>
<p class="lead abs" style="top:962px">At Tallowreach, we are focused on your mental wellness. Tallowreach is open to anyone looking for an Online or Gold Coast Psychologist to help them overcome barriers and find fulfilment in their lives. We also offer do it yourself educational programs.</p>

<div class="photo abs" style="left:111px;top:1120px;width:424px;height:493px;background:linear-gradient(160deg,#dcdcdc,#a89c95 60%,#3a3a3a)" role="img" aria-label="Portrait of the psychologist"></div>
<div class="script abs">I am Owen Calder</div>
<div class="sub abs" style="left:610px;top:1190px;width:470px">An experienced Gold Coast Psychologist, also available online.</div>
<p class="body abs" style="left:610px;top:1272px;width:485px">Unfortunately, we all go through periods of crisis in our lives. When we find ourselves struggling for an extended period, we can use bit of help to work through barriers that stand in our way. Counselling or psychotherapy can help. Contact Owen, your Gold Coast Psychologist.</p>
<p class="body abs" style="left:610px;top:1426px;width:485px">Owen has 15 years experience in providing counselling and psychotherapy to people from all of walks of life. Owen understands the different challenges that people of all backgrounds face in coming to seek help and has a variety of treatments to help.</p>
<a class="btn btn-line abs" style="left:610px;top:1565px;width:167px">ONLINE HELP</a>

<svg class="wave abs" style="top:1670px" width="1200" height="140" viewBox="0 0 1200 140"><path d="M0 60 C200 -10 380 90 620 60 C850 30 1000 20 1200 50 L1200 140 L0 140Z" fill="var(--sand)"/></svg>
<div class="abs" style="left:0;top:1800px;width:1200px;height:660px;background:var(--sand)"></div>

<div class="label abs" style="top:1866px;left:111px;width:auto;text-align:left">SERVICES</div>
<h2 class="services-title abs">PSYCHOLOGICAL<br>COUNSELLING</h2>
<p class="body abs" style="left:111px;top:2037px;width:510px">Tallowreach can provide assistance in the assessment and treatment of psychological and mental health problems related to:</p>
<div class="list abs">
  <span><svg width="14" height="12" viewBox="0 0 14 12"><path d="M1 6l4 4 8-9" stroke="var(--accent)" stroke-width="2.5" fill="none"/></svg>Anxiety</span>
  <span><svg width="14" height="12" viewBox="0 0 14 12"><path d="M1 6l4 4 8-9" stroke="var(--accent)" stroke-width="2.5" fill="none"/></svg>Self Esteem</span>
  <span><svg width="14" height="12" viewBox="0 0 14 12"><path d="M1 6l4 4 8-9" stroke="var(--accent)" stroke-width="2.5" fill="none"/></svg>Depression</span>
  <span><svg width="14" height="12" viewBox="0 0 14 12"><path d="M1 6l4 4 8-9" stroke="var(--accent)" stroke-width="2.5" fill="none"/></svg>ADD</span>
  <span><svg width="14" height="12" viewBox="0 0 14 12"><path d="M1 6l4 4 8-9" stroke="var(--accent)" stroke-width="2.5" fill="none"/></svg>Stress</span>
  <span><svg width="14" height="12" viewBox="0 0 14 12"><path d="M1 6l4 4 8-9" stroke="var(--accent)" stroke-width="2.5" fill="none"/></svg>Work Related Stress</span>
  <span><svg width="14" height="12" viewBox="0 0 14 12"><path d="M1 6l4 4 8-9" stroke="var(--accent)" stroke-width="2.5" fill="none"/></svg>Dating &amp; Relationships</span>
  <span><svg width="14" height="12" viewBox="0 0 14 12"><path d="M1 6l4 4 8-9" stroke="var(--accent)" stroke-width="2.5" fill="none"/></svg>Trauma and EMDR</span>
</div>
<a class="btn btn-line abs" style="left:111px;top:2290px;width:168px">READ MORE</a>
<div class="abs" style="left:654px;top:1847px;width:546px;height:500px;border-radius:260px 0 0 260px;background:linear-gradient(135deg,#8a7a68,#c9c3b8 50%,#3b3d40)" role="img" aria-label="Counselling session with the psychologist talking to a client"></div>

<svg class="wave abs" style="top:2400px" width="1200" height="80" viewBox="0 0 1200 80"><path d="M0 50 C250 0 500 20 700 45 C900 70 1050 30 1200 20 L1200 80 L0 80Z" fill="var(--mist)"/></svg>
<section class="band abs"></section>
<div class="label abs" style="top:2597px">USEFUL LINKS</div>
<h2 class="heading abs" style="top:2640px">CURRENT FREE TRAINING PROGRAMS</h2>
<div class="cards abs">
  <div class="card">Map your<br>Bearings</div>
  <div class="card">Lantern and<br>Compass Workbook</div>
  <div class="card">Quiet Harbour<br>Program</div>
  <div class="card">Relationship<br>Assessment Tool</div>
</div>

<section class="courses abs"></section>
<div class="label abs" style="top:2993px">COURSES</div>
<h2 class="heading abs" style="top:3036px">UPCOMING PROGRAMS</h2>
<article class="course abs" style="left:111px;top:3141px">
  <div class="course-img" style="background:linear-gradient(135deg,#c9cfc8,#8a8c83 55%,#d9b45c)" role="img" aria-label="Older man reading on a phone on a sofa"></div>
  <h3>Where Did All the Summers Go?</h3>
  <h4>Healthy Mindset for a Healthy Love Life</h4>
  <p>FREE 3 part live training series series <a>running September</a></p>
</article>
<article class="course abs" style="left:634px;top:3141px">
  <div class="course-img" style="background:linear-gradient(135deg,#d8d4cc,#a7a39b 55%,#c58f50)" role="img" aria-label="Woman on a sofa with a laptop and earphones"></div>
  <h3>Getting Unstuck</h3>
  <h4>Tending the Willow Garden Masterclass</h4>
  <p><a>Register Your Interest</a></p>
</article>

<div class="label abs" style="top:3760px">CONTACT US</div>
<h2 class="heading abs" style="top:3806px">GET IN TOUCH</h2>
<p class="lead abs" style="top:3880px;left:205px;width:790px;line-height:28px">Expect a response within 24 hours. Any contact made is via a secure server and will be treated confidentially. Your information and contact details will NEVER be given to any third party, nor will you be subscribed to any kind of mailing list. Please DO NOT email us for website or SEO offers.</p>
<div class="field abs" style="left:181px;top:4013px;width:412px;height:53px">Your Name (required)</div>
<div class="field abs" style="left:181px;top:4081px;width:412px;height:53px">Your Email (required)</div>
<div class="field abs" style="left:181px;top:4151px;width:412px;height:53px">Your Phone</div>
<div class="field abs" style="left:609px;top:4013px;width:411px;height:191px">Your Message</div>
<a class="btn btn-line abs" style="left:538px;top:4260px;width:124px">SUBMIT</a>
<div class="abs" style="left:0;top:4125px;width:150px;height:270px;background:linear-gradient(180deg,rgba(42,157,189,.8),rgba(42,157,189,.5))" role="img" aria-label="Palm tree silhouette decoration"></div>
<svg class="wave abs" style="top:4330px" width="1200" height="220" viewBox="0 0 1200 220"><path d="M0 60 C300 20 600 120 900 70 C1050 45 1130 40 1200 45 L1200 220 L0 220Z" fill="#fff"/><path d="M40 80 C300 40 600 130 900 85" stroke="rgba(42,157,189,.25)" stroke-width="4" fill="none"/></svg>
<div class="abs" style="left:0;top:4480px;width:1200px;height:436px;background:#fff"></div>

<footer class="footer abs">
  <div class="badge" style="top:60px;width:150px;height:38px;background:#5aa43c;border-radius:3px"></div>
  <div class="badge" style="top:118px;width:116px;height:84px;background:#b7cde0;border-radius:3px"></div>
  <div class="badge" style="top:222px;width:146px;height:66px;background:#c9a0a8;border-radius:3px"></div>
</footer>
<div class="fcol" style="left:345px">
  <h5>Information</h5>
  <p>Home</p><p>About</p><p>Counselling &amp; Therapy</p><p>Current FREE Training Programs</p><p>Courses</p><p>Blog</p><p>Contact</p><p>Bookings</p>
</div>
<div class="fcol" style="left:620px">
  <h5>Quick Links</h5>
  <p>Privacy Policy</p><p>Cookie Policy</p><p>Terms And Conditions</p>
</div>
<div class="fcol" style="left:834px">
  <h5>Contact information</h5>
  <p><svg width="12" height="16" viewBox="0 0 12 16"><path d="M6 0a6 6 0 0 0-6 6c0 4.5 6 10 6 10s6-5.5 6-10a6 6 0 0 0-6-6zm0 8.5A2.5 2.5 0 1 1 6 3.5a2.5 2.5 0 0 1 0 5z" fill="var(--accent)"/></svg>48 Driftwood Pde. Seabrook</p>
  <p style="margin-top:14px"><svg width="14" height="14" viewBox="0 0 14 14"><path d="M3 1l2 3-1.5 1.5a8 8 0 0 0 5 5L10 9l3 2-1.5 2.5C6 13 1 8 .5 2.5z" fill="var(--accent)"/></svg>0400 118 327</p>
  <p style="margin-top:14px"><svg width="14" height="14" viewBox="0 0 14 14"><rect x="1" y="4" width="12" height="9" rx="1" fill="var(--accent)"/><rect x="4" y="1" width="6" height="4" fill="var(--accent)"/></svg>(07) 5550 1180</p>
  <p style="margin-top:14px"><svg width="14" height="14" viewBox="0 0 14 14"><circle cx="7" cy="7" r="6" stroke="var(--accent)" stroke-width="1.8" fill="none"/><path d="M7 3.5V7l2.5 1.5" stroke="var(--accent)" stroke-width="1.6" fill="none"/></svg>8:00am - 7:00pm (appt. Only)</p>
</div>

<div class="bar abs">
  <span>Copyright © 2024, Tallowreach.</span>
  <div class="brand"><span class="brand-dot"></span><span class="brand-name">Tallowreach</span></div>
  <div class="social"><span></span><span></span></div>
</div>

</body>
</html>
```